Corvane Supplies Business Card

Professional business card that stand out to our potential customers. Front and back with clean modern design

Industry/Entity Type

Oil and gas

Contact Information for Business Card

Name, address, website , office phone and cell number

Requirements
Must have
• Editable files for each employee

```html
<!DOCTYPE html>
<html lang="en">
<head>
<meta charset="utf-8">
<title>Corvane Supplies Business Card</title>
<link href="https://fonts.googleapis.com/css2?family=Open+Sans:wght@400;800&display=swap" rel="stylesheet">
<style>
  :root {
    --page: #ffffff;
    --navy-light: #112a47;
    --navy-dark: #01142b;
    --cyan: #05afd2;
    --red: #f50f0f;
    --ink: #141414;
    --card-white: #fdfdfd;
    --pattern-grey: #f1f1f1;
  }
  * { box-sizing: border-box; margin: 0; padding: 0; }
  html, body { width: 1100px; height: 1200px; overflow: hidden; background: var(--page); }
  body { position: relative; font-family: "Open Sans", Arial, sans-serif; }

  .card {
    position: absolute;
    left: 116px;
    width: 873px;
    height: 476px;
    box-shadow: 0 16px 28px rgba(0, 0, 0, 0.28);
    overflow: hidden;
  }
  .card-front { top: 63px; }
  .card-back { top: 666px; }

  .card-surface { position: absolute; inset: 0; }
  .card-front .card-surface {
    background: linear-gradient(90deg, var(--navy-light) 0%, var(--navy-dark) 45%, var(--navy-dark) 100%);
  }
  .card-back .card-surface {
    background: linear-gradient(180deg, var(--card-white), var(--pattern-grey));
  }

  .brand-name {
    position: absolute;
    left: 0; right: 0;
    text-align: center;
    font-weight: 800;
    text-transform: uppercase;
    letter-spacing: 1px;
    display: flex;
    align-items: center;
    justify-content: center;
    gap: 14px;
  }
  .brand-mark { display: inline-block; background: var(--red); }
  .card-front .brand-name { top: 210px; font-size: 44px; color: #ffffff; }
  .card-front .brand-mark { width: 34px; height: 34px; }
  .card-back .brand-name {
    left: 40px; right: auto; width: 356px;
    top: 220px; font-size: 27px; color: var(--ink);
  }
  .card-back .brand-mark { width: 22px; height: 22px; }

  .divider {
    position: absolute;
    left: 437px; top: 119px;
    width: 2px; height: 238px;
    background: var(--cyan);
  }

  .contact {
    position: absolute;
    left: 542px; top: 110px;
    width: 226px;
    text-align: center;
    color: var(--ink);
  }
  .company-label { font-size: 27px; line-height: 1.2; white-space: nowrap; margin-left: -20px; margin-right: -20px; }
  .icon-rule { display: block; margin: 18px auto 12px; }
  .contact-line { line-height: 1.2; white-space: nowrap; }
  .line-lg { font-size: 20px; }
  .line-md { font-size: 17px; margin-top: 3px; }
  .line-sm { font-size: 16px; margin-top: 5px; }
</style>
</head>
<body>

<section class="card card-front">
  <div class="card-surface" role="img" aria-label="Dark navy background with a faint geometric star pattern"></div>
  <div class="brand-name"><span class="brand-mark"></span>Corvane Supplies</div>
</section>

<section class="card card-back">
  <div class="card-surface" role="img" aria-label="White background with a faint light grey geometric star pattern"></div>
  <div class="brand-name"><span class="brand-mark"></span>Corvane Supplies</div>

  <div class="divider"></div>

  <div class="contact">
    <p class="company-label">COMPANY NAME</p>
    <svg class="icon-rule" width="226" height="22" viewBox="0 0 226 22" aria-hidden="true">
      <line x1="0" y1="11" x2="226" y2="11" stroke="#05afd2" stroke-width="1.6"/>
      <g fill="#05afd2">
        <circle cx="61" cy="11" r="10"/>
        <circle cx="87" cy="11" r="10"/>
        <circle cx="113" cy="11" r="10"/>
        <circle cx="140" cy="11" r="10"/>
        <circle cx="166" cy="11" r="10"/>
      </g>
      <g fill="#ffffff" stroke="#ffffff">
        <!-- phone -->
        <path d="M57 6 l2.5 0 l1 3 l-1.5 1.2 a7 7 0 0 0 3 3 l1.2 -1.5 l3 1 l0 2.5 a1.3 1.3 0 0 1 -1.4 1 a10 10 0 0 1 -8.8 -8.8 a1.3 1.3 0 0 1 1 -1.4z" stroke="none"/>
        <!-- desk telephone -->
        <path d="M81.5 9 a8 5 0 0 1 11 0 l0 1.6 l-2.6 0 l0 -1.2 a5 3 0 0 0 -5.8 0 l0 1.2 l-2.6 0z" stroke="none"/>
        <rect x="83" y="11" width="8" height="5" rx="1" stroke="none"/>
        <!-- pin -->
        <path d="M113 5 a4.5 4.5 0 0 1 4.5 4.5 c0 3 -4.5 7.5 -4.5 7.5 s-4.5 -4.5 -4.5 -7.5 a4.5 4.5 0 0 1 4.5 -4.5z" stroke="none"/>
        <circle cx="113" cy="9.5" r="1.7" fill="#05afd2" stroke="none"/>
        <!-- mail -->
        <rect x="134.5" y="7" width="11" height="8" fill="none" stroke-width="1.3"/>
        <polyline points="134.5,7 140,11.5 145.5,7" fill="none" stroke-width="1.3"/>
        <!-- globe -->
        <circle cx="166" cy="11" r="5.5" fill="none" stroke-width="1.1"/>
        <ellipse cx="166" cy="11" rx="2.4" ry="5.5" fill="none" stroke-width="1"/>
        <line x1="160.5" y1="11" x2="171.5" y2="11" stroke-width="1"/>
      </g>
    </svg>
    <p class="contact-line line-lg">012 345 6789</p>
    <p class="contact-line line-md">012 345 6789</p>
    <p class="contact-line line-lg">addresscityname000</p>
    <p class="contact-line line-sm">youremail@corvane.com</p>
    <p class="contact-line line-md">www.yourwebsite.com</p>
  </div>
</section>

</body>
</html>
```